ASL Learning Website Application Pages Redesign

Introduction:
We need a redesign of the internal pages of our website, SignTrellis.com. The current website design has been in place for many years and is not mobile friendly. We want an updated design that makes the site look cleaner, more professional, and mobile accessible. We are looking for a design that eliminates the clutter on each page, and makes the site simple and easy to use. We will be interested in your design if it is unique and creative. Don't be afraid to completely change the look of the site.

We need the designs sliced up into clean HTML files that are responsive and work well on both mobile and desktop computers. We will implement the PHP needed to make the pages functional.

About Us:
SignTrellis is a subscription-based website for American Sign Language (ASL) video lessons. The content is for anyone who wishes to learn ASL, regardless of age. It has been designed to instruct Deaf students, parents of Deaf children, and the community-at-large. All lessons are taught by Deaf experts of ASL.

Overview:
The website before log-in does not need any changes. There are five key pages within the internal website (after log-in) that need to be redesigned; they are listed below. Note that some pages (Dictionary and Activity) have multiple sub-pages, so there are about 6-8 pages in total to design, depending on how you decide to approach this (more info in the pages’ respective instruction documents).

The new page designs should retain their existing features, and as stated before, should be mobile friendly. However, you may combine, collapse, or completely change the look of these features. Each page to redesign has a separate instruction document attachment, and screenshots of the current version of the page. Our logo has also been attached. If you want to see the website pages for yourself, you can also go to our website (SignTrellis.com) and use a free trial to get access to the internal site.

As for design preferences, we want our site to be modern-looking and mature. We’re looking for an inviting, educational style that can attract both high school students and adults. We’re happy with the current font and color scheme, but we’re always open to ideas!

Additional Notes:
- Every page has the same header and footer. You could keep these the same, or change them, based on your discretion.
- Currently, every page also has a breadcrumb. The breadcrumb is unnecessary and you may remove it. However, the “add/remove from favorites” button on the right of the breadcrumb is necessary to keep somewhere on the page.

Pages:
Here’s a list of the five key pages we need redesigned:
- Dashboard
- Dictionary
- Lesson
- Activity
- All Lessons

Each page has its own instruction document. These are attached separately.

Just purchased a $150 for Top designers. I need to give them time to submit their designs . Can I have 7 more days?

Target Market(s)

Deaf students, parents of Deaf children, and the community-at-large interested in learning ASL

Coding

Coded - Design and coding required

Number of Pages Required

5+ page

Font styles to use
Sans Serif

Requirements
Must have
• Responsive design - the full application experience should be available on mobile devices.
Follow the directions on the design brief.
Nice to have
• Be creative! Please play around with, or even completely change, the look of the site.

```html
<!DOCTYPE html>
<html lang="en">
<head>
<meta charset="utf-8">
<title>SignTrellis – All Lessons</title>
<link href="https://fonts.googleapis.com/css2?family=Lato:ital,wght@0,400;0,700;1,400&display=swap" rel="stylesheet">
<style>
:root{
  --canvas:#f0f0f0;
  --white:#ffffff;
  --ink:#222222;
  --muted:#777777;
  --green:#5aaa32;
  --green-bright:#62b53a;
  --nav:#111111;
  --line:#dddddd;
  --soft:#f7f7f7;
  --side:#e9e9e9;
  --beige:#faf3e4;
}
*{box-sizing:border-box;margin:0;padding:0}
html,body{width:1200px;height:1114px;overflow:hidden;background:var(--canvas);font-family:'Lato',sans-serif;color:var(--ink)}
.page{position:absolute;top:81px;width:480px;height:949px;background:var(--white);box-shadow:0 0 4px rgba(0,0,0,.06)}
.page--classic{left:77px}
.page--accent{left:643px}

.site-header{height:48px;display:flex;align-items:center;position:relative}
.brand{display:flex;align-items:center;gap:4px;padding-left:45px;width:165px;height:100%}
.brand-dot{width:12px;height:12px;border-radius:50%;background:var(--green)}
.brand-name{font-size:17px;font-weight:700;color:var(--ink)}
.tagline{padding-left:28px}
.tagline h1{font-size:9px;font-weight:700;color:#333;letter-spacing:.1px}
.tagline p{font-size:6.5px;font-style:italic;color:var(--muted);margin-top:4px}
.page--accent .brand{background:var(--beige)}
.page--accent .tagline{background:var(--green-bright);flex:1;height:100%;display:flex;flex-direction:column;justify-content:center;position:relative}
.page--accent .tagline::before{content:"";position:absolute;left:0;top:18px;border-left:6px solid var(--beige);border-top:6px solid transparent;border-bottom:6px solid transparent}
.page--accent .tagline h1,.page--accent .tagline p{color:var(--white)}

.main-nav{height:21px;background:var(--nav);display:flex;justify-content:center;align-items:center;gap:16px}
.main-nav a{font-size:7px;color:var(--white);text-decoration:none}
.main-nav a.is-active{color:var(--green-bright)}

.content{padding:0 45px}
.breadcrumb{font-size:7.5px;color:var(--muted);padding-top:11px;height:29px;border-bottom:1px solid var(--line)}
.breadcrumb .current{color:var(--green)}
.title-row{display:flex;align-items:center;margin-top:13px;height:23px}
.title-row h2{font-size:13.5px;font-weight:400;width:105px}
.search{flex:1;display:flex;height:23px;border:1px solid #cfcfcf}
.search-field{flex:1;display:flex;align-items:center;gap:4px;padding-left:8px;font-size:6.5px;color:var(--muted)}
.search-btn{width:70px;background:var(--green);color:var(--white);font-size:6.8px;display:flex;align-items:center;justify-content:center}

.catalog{display:flex;margin-top:24px}
.levels{width:90px;height:384px;border:1px solid var(--line);list-style:none;margin-right:15px}
.levels li{height:20px;line-height:20px;padding-left:12px;font-size:6.5px;color:#333}
.levels li.is-active{background:var(--side)}
.lesson-grid{display:grid;grid-template-columns:repeat(3,92px);grid-auto-rows:101px;column-gap:5px;row-gap:5.5px}
.lesson-card{background:var(--white);box-shadow:0 0 3px rgba(0,0,0,.12);text-align:center}
.thumb{height:73px}
.lesson-card h3{font-size:8px;font-weight:400;margin-top:4px}
.lesson-card p{font-size:6.3px;font-style:italic;color:var(--muted);margin-top:2px}

.pager{display:flex;margin:18px 0 0 105px;height:19px}
.pager span{width:20.5px;border:1px solid var(--line);margin-left:-1px;font-size:7.5px;color:#555;display:flex;align-items:center;justify-content:center}
.pager span.is-current{background:#aaaaaa;color:var(--white);border-color:#aaa}

.site-footer{position:absolute;left:0;right:0;bottom:0;height:192px;background:var(--soft);padding:14px 45px 0}
.footer-cols{display:flex;height:126px}
.footer-about{width:177px}
.footer-about .brand{padding-left:0;width:auto;height:34px}
.footer-about p{font-size:6px;line-height:10px;color:#555;width:148px;margin-top:2px}
.footer-col h4{font-size:8.5px;font-weight:400;margin-top:21px;margin-bottom:9px}
.quick{width:86px}
.quick a{display:block;font-size:6px;color:#555;line-height:10px;text-decoration:none}
.contact-row{display:flex;align-items:center;gap:5px;font-size:6.2px;color:#555;margin-left:-3px;margin-bottom:5px}
.icon-ring{width:15px;height:15px;border:1px solid #ccc;border-radius:50%;display:flex;align-items:center;justify-content:center}
.footer-bottom{border-top:1px solid var(--line);margin-top:16px;padding-top:9px;display:flex;justify-content:space-between;align-items:center}
.footer-bottom p{font-size:6.3px;color:#555}
.socials{display:flex;gap:2px}
.socials span{width:16px;height:16px;border:1px solid #bbb;border-radius:50%;display:flex;align-items:center;justify-content:center}
.socials span::after{content:"";width:5px;height:5px;border-radius:50%;background:var(--green)}
</style>
</head>
<body>

<!-- Page variant: white header -->
<section class="page page--classic">
  <header class="site-header">
    <div class="brand"><span class="brand-dot"></span><span class="brand-name">SignTrellis</span></div>
    <div class="tagline"><h1>LEARN ASL THROUGH VIDEO LESSONS ONLINE</h1><p>You are currently logged in as: Marisol</p></div>
  </header>
  <nav class="main-nav"><a>Dashboard</a><a class="is-active">Lessons</a><a>Lesson List</a><a>Dictionary</a><a>Handshapes</a><a>Locations</a><a>Update Account</a><a>Logout</a></nav>
  <div class="content">
    <div class="breadcrumb">SignTrellis &gt; <span class="current">All Lessons</span></div>
    <div class="title-row"><h2>All Lessons</h2>
      <div class="search"><div class="search-field"><svg width="7" height="7" viewBox="0 0 10 10"><circle cx="4" cy="4" r="3" fill="none" stroke="#555" stroke-width="1.4"/><line x1="6.3" y1="6.3" x2="9" y2="9" stroke="#555" stroke-width="1.4"/></svg>Search all lessons</div><div class="search-btn">SEARCH LESSSON</div></div>
    </div>
    <div class="catalog">
      <ul class="levels"><li class="is-active">Beginner</li><li>Intermediate</li><li>Advanced</li><li>Advanced Plus</li><li>5th Level</li><li>Interpreter Section</li><li>Warm Ups</li><li>Holidays</li><li>Verbs</li><li>Time</li><li>Numbers</li><li>Food</li><li>Money</li><li>House</li><li>Medical Related</li><li>Stories</li><li>Deaf Culture</li><li>Fingerspelling</li><li>Deaf And Blind</li></ul>
      <div class="lesson-grid">
        <article class="lesson-card"><div class="thumb" role="img" aria-label="Colourful scattered letters" style="background:linear-gradient(135deg,#f4f4f4,#e8e3d8)"></div><h3>Alphabet</h3><p>Beginner</p></article>
        <article class="lesson-card"><div class="thumb" role="img" aria-label="Hand placing greeting letter blocks" style="background:linear-gradient(180deg,#5aa23a,#e8dcd0)"></div><h3>Meet &amp; Greet</h3><p>Beginner</p></article>
        <article class="lesson-card"><div class="thumb" role="img" aria-label="Rainbow coloured numbers" style="background:linear-gradient(135deg,#e94b7a,#f2d13a,#3fb0c9,#7bd14a)"></div><h3>Numbers 1-20</h3><p>Beginner, Numbers</p></article>
        <article class="lesson-card"><div class="thumb" role="img" aria-label="Hands using a calculator" style="background:linear-gradient(135deg,#eef0f2,#8a8f96)"></div><h3>Math Number Challenge</h3><p>Beginner, Numbers</p></article>
        <article class="lesson-card"><div class="thumb" role="img" aria-label="Explosion of coloured powder" style="background:radial-gradient(circle,#e8419b,#3a6ad8 55%,#111 90%)"></div><h3>Colors</h3><p>Beginner</p></article>
        <article class="lesson-card"><div class="thumb" role="img" aria-label="Red first aid kit" style="background:linear-gradient(135deg,#d62b35,#9a1d24 60%,#d8d8d8)"></div><h3>Survival Words</h3><p>Beginner</p></article>
        <article class="lesson-card"><div class="thumb" role="img" aria-label="Hands signing" style="background:linear-gradient(180deg,#d9d9d9,#8a7060)"></div><h3>Deaf Culture 1</h3><p>Beginner, Deaf Culture</p></article>
        <article class="lesson-card"><div class="thumb" role="img" aria-label="Hand forming a sign" style="background:linear-gradient(135deg,#6d747b,#c9b9ad)"></div><h3>Fingerspelling 1</h3><p>Beginner, Fingerspelling</p></article>
        <article class="lesson-card"><div class="thumb" role="img" aria-label="Family jumping on a beach at sunset" style="background:linear-gradient(180deg,#f6c26a,#c25a3a 60%,#5a2a20)"></div><h3>Family</h3><p>Beginner</p></article>
        <article class="lesson-card"><div class="thumb" role="img" aria-label="Stacked hands" style="background:linear-gradient(135deg,#c89a7a,#e9e2d8)"></div><h3>Pronouns</h3><p>Beginner</p></article>
        <article class="lesson-card"><div class="thumb" role="img" aria-label="Dice showing the word verb" style="background:linear-gradient(135deg,#3a3a3a,#f0e8e0 55%,#2a2a2a)"></div><h3>Verbs 1</h3><p>Beginner, Verbs</p></article>
        <article class="lesson-card"><div class="thumb" role="img" aria-label="Road signs for synonym and antonym" style="background:linear-gradient(180deg,#9aa0a6,#c8cccf 60%,#5c8ed6)"></div><h3>Antonyms &amp; Synonyms 1</h3><p>Beginner</p></article>
        <article class="lesson-card"><div class="thumb" role="img" aria-label="Raised hands under question marks" style="background:linear-gradient(180deg,#f0f0f0,#e47a5a 60%,#d8b0a0)"></div><h3>Classroom Essentials 1</h3><p>Beginner</p></article>
        <article class="lesson-card"><div class="thumb" role="img" aria-label="Question mark speech bubbles" style="background:linear-gradient(135deg,#1fb8d6,#f5c53a 55%,#1fb8d6)"></div><h3>Quiz 1</h3><p>Beginner</p></article>
        <article class="lesson-card"><div class="thumb" role="img" aria-label="Raised index finger on black" style="background:radial-gradient(circle at 55% 55%,#8a6050,#111 60%)"></div><h3>Handshape Quiz 1</h3><p>Beginner</p></article>
      </div>
    </div>
    <div class="pager"><span class="is-current">1</span><span>2</span><span>3</span><span>4</span><span>5</span><span>6</span><span>7</span></div>
  </div>
  <footer class="site-footer">
    <div class="footer-cols">
      <div class="footer-about"><div class="brand"><span class="brand-dot"></span><span class="brand-name">SignTrellis</span></div>
        <p>SignTrellis is a subscription based website for American Sign Language (ASL) video lessons. The content is for anyone who wishes to learn ASL, regardless of age. It has been designed to instruct Deaf students, parents of Deaf children, and the community-at-large. You may cancel your subscription at any time. All lessons are taught by Deaf experts of ASL.</p></div>
      <div class="footer-col quick"><h4>Quick Links</h4><a>Home</a><a>Try it Free</a><a>Contact Us</a><a>Group Rate Form</a><a>Teacher's Guide</a><a>Gift Certificates</a><a>FAQs</a><a>Privacy Policy</a></div>
      <div class="footer-col"><h4>Contact Us</h4>
        <div class="contact-row"><span class="icon-ring"><svg width="6" height="8" viewBox="0 0 6 8"><path d="M3 8C1 5 0 4 0 3a3 3 0 0 1 6 0c0 1-1 2-3 5z" fill="#5aaa32"/></svg></span>PO Box 50872, Cedar Falls, MI 48990</div>
        <div class="contact-row"><span class="icon-ring"><svg width="7" height="7" viewBox="0 0 10 10"><path d="M2 0l2 2-1 2c1 1 2 2 3 3l2-1 2 2-2 2C4 10 0 6 0 2z" fill="#5aaa32"/></svg></span>(555) 014-2290</div>
        <div class="contact-row"><span class="icon-ring"><svg width="7" height="5" viewBox="0 0 10 7"><rect width="10" height="7" fill="#5aaa32"/><path d="M0 0l5 4 5-4" fill="none" stroke="#fff"/></svg></span>info@signtrellis.com</div>
      </div>
    </div>
    <div class="footer-bottom"><p>Copyrights © 2021, SignTrellis. All rights reserved. Terms &amp; Conditions</p><div class="socials"><span></span><span></span><span></span><span></span><span></span></div></div>
  </footer>
</section>

<!-- Page variant: green header -->
<section class="page page--accent">
  <header class="site-header">
    <div class="brand"><span class="brand-dot"></span><span class="brand-name">SignTrellis</span></div>
    <div class="tagline"><h1>LEARN ASL THROUGH VIDEO LESSONS ONLINE</h1><p>You are currently logged in as: Marisol</p></div>
  </header>
  <nav class="main-nav"><a>Dashboard</a><a class="is-active">Lessons</a><a>Lesson List</a><a>Dictionary</a><a>Handshapes</a><a>Locations</a><a>Update Account</a><a>Logout</a></nav>
  <div class="content">
    <div class="breadcrumb">SignTrellis &gt; <span class="current">All Lessons</span></div>
    <div class="title-row"><h2>All Lessons</h2>
      <div class="search"><div class="search-field"><svg width="7" height="7" viewBox="0 0 10 10"><circle cx="4" cy="4" r="3" fill="none" stroke="#555" stroke-width="1.4"/><line x1="6.3" y1="6.3" x2="9" y2="9" stroke="#555" stroke-width="1.4"/></svg>Search all lessons</div><div class="search-btn">SEARCH LESSSON</div></div>
    </div>
    <div class="catalog">
      <ul class="levels"><li class="is-active">Beginner</li><li>Intermediate</li><li>Advanced</li><li>Advanced Plus</li><li>5th Level</li><li>Interpreter Section</li><li>Warm Ups</li><li>Holidays</li><li>Verbs</li><li>Time</li><li>Numbers</li><li>Food</li><li>Money</li><li>House</li><li>Medical Related</li><li>Stories</li><li>Deaf Culture</li><li>Fingerspelling</li><li>Deaf And Blind</li></ul>
      <div class="lesson-grid">
        <article class="lesson-card"><div class="thumb" role="img" aria-label="Colourful scattered letters" style="background:linear-gradient(135deg,#f4f4f4,#e8e3d8)"></div><h3>Alphabet</h3><p>Beginner</p></article>
        <article class="lesson-card"><div class="thumb" role="img" aria-label="Hand placing greeting letter blocks" style="background:linear-gradient(180deg,#5aa23a,#e8dcd0)"></div><h3>Meet &amp; Greet</h3><p>Beginner</p></article>
        <article class="lesson-card"><div class="thumb" role="img" aria-label="Rainbow coloured numbers" style="background:linear-gradient(135deg,#e94b7a,#f2d13a,#3fb0c9,#7bd14a)"></div><h3>Numbers 1-20</h3><p>Beginner, Numbers</p></article>
        <article class="lesson-card"><div class="thumb" role="img" aria-label="Hands using a calculator" style="background:linear-gradient(135deg,#eef0f2,#8a8f96)"></div><h3>Math Number Challenge</h3><p>Beginner, Numbers</p></article>
        <article class="lesson-card"><div class="thumb" role="img" aria-label="Explosion of coloured powder" style="background:radial-gradient(circle,#e8419b,#3a6ad8 55%,#111 90%)"></div><h3>Colors</h3><p>Beginner</p></article>
        <article class="lesson-card"><div class="thumb" role="img" aria-label="Red first aid kit" style="background:linear-gradient(135deg,#d62b35,#9a1d24 60%,#d8d8d8)"></div><h3>Survival Words</h3><p>Beginner</p></article>
        <article class="lesson-card"><div class="thumb" role="img" aria-label="Hands signing" style="background:linear-gradient(180deg,#d9d9d9,#8a7060)"></div><h3>Deaf Culture 1</h3><p>Beginner, Deaf Culture</p></article>
        <article class="lesson-card"><div class="thumb" role="img" aria-label="Hand forming a sign" style="background:linear-gradient(135deg,#6d747b,#c9b9ad)"></div><h3>Fingerspelling 1</h3><p>Beginner, Fingerspelling</p></article>
        <article class="lesson-card"><div class="thumb" role="img" aria-label="Family jumping on a beach at sunset" style="background:linear-gradient(180deg,#f6c26a,#c25a3a 60%,#5a2a20)"></div><h3>Family</h3><p>Beginner</p></article>
        <article class="lesson-card"><div class="thumb" role="img" aria-label="Stacked hands" style="background:linear-gradient(135deg,#c89a7a,#e9e2d8)"></div><h3>Pronouns</h3><p>Beginner</p></article>
        <article class="lesson-card"><div class="thumb" role="img" aria-label="Dice showing the word verb" style="background:linear-gradient(135deg,#3a3a3a,#f0e8e0 55%,#2a2a2a)"></div><h3>Verbs 1</h3><p>Beginner, Verbs</p></article>
        <article class="lesson-card"><div class="thumb" role="img" aria-label="Road signs for synonym and antonym" style="background:linear-gradient(180deg,#9aa0a6,#c8cccf 60%,#5c8ed6)"></div><h3>Antonyms &amp; Synonyms 1</h3><p>Beginner</p></article>
        <article class="lesson-card"><div class="thumb" role="img" aria-label="Raised hands under question marks" style="background:linear-gradient(180deg,#f0f0f0,#e47a5a 60%,#d8b0a0)"></div><h3>Classroom Essentials 1</h3><p>Beginner</p></article>
        <article class="lesson-card"><div class="thumb" role="img" aria-label="Question mark speech bubbles" style="background:linear-gradient(135deg,#1fb8d6,#f5c53a 55%,#1fb8d6)"></div><h3>Quiz 1</h3><p>Beginner</p></article>
        <article class="lesson-card"><div class="thumb" role="img" aria-label="Raised index finger on black" style="background:radial-gradient(circle at 55% 55%,#8a6050,#111 60%)"></div><h3>Handshape Quiz 1</h3><p>Beginner</p></article>
      </div>
    </div>
    <div class="pager"><span class="is-current">1</span><span>2</span><span>3</span><span>4</span><span>5</span><span>6</span><span>7</span></div>
  </div>
  <footer class="site-footer">
    <div class="footer-cols">
      <div class="footer-about"><div class="brand"><span class="brand-dot"></span><span class="brand-name">SignTrellis</span></div>
        <p>SignTrellis is a subscription based website for American Sign Language (ASL) video lessons. The content is for anyone who wishes to learn ASL, regardless of age. It has been designed to instruct Deaf students, parents of Deaf children, and the community-at-large. You may cancel your subscription at any time. All lessons are taught by Deaf experts of ASL.</p></div>
      <div class="footer-col quick"><h4>Quick Links</h4><a>Home</a><a>Try it Free</a><a>Contact Us</a><a>Group Rate Form</a><a>Teacher's Guide</a><a>Gift Certificates</a><a>FAQs</a><a>Privacy Policy</a></div>
      <div class="footer-col"><h4>Contact Us</h4>
        <div class="contact-row"><span class="icon-ring"><svg width="6" height="8" viewBox="0 0 6 8"><path d="M3 8C1 5 0 4 0 3a3 3 0 0 1 6 0c0 1-1 2-3 5z" fill="#5aaa32"/></svg></span>PO Box 50872, Cedar Falls, MI 48990</div>
        <div class="contact-row"><span class="icon-ring"><svg width="7" height="7" viewBox="0 0 10 10"><path d="M2 0l2 2-1 2c1 1 2 2 3 3l2-1 2 2-2 2C4 10 0 6 0 2z" fill="#5aaa32"/></svg></span>(555) 014-2290</div>
        <div class="contact-row"><span class="icon-ring"><svg width="7" height="5" viewBox="0 0 10 7"><rect width="10" height="7" fill="#5aaa32"/><path d="M0 0l5 4 5-4" fill="none" stroke="#fff"/></svg></span>info@signtrellis.com</div>
      </div>
    </div>
    <div class="footer-bottom"><p>Copyrights © 2021, SignTrellis. All rights reserved. Terms &amp; Conditions</p><div class="socials"><span></span><span></span><span></span><span></span><span></span></div></div>
  </footer>
</section>

</body>
</html>
```